Home Design company focused on remodel and enhancement of kitchens and bathroorms

I already have a logo designed by ArtHarbor, I now need a design for my business cards.
The company is in the remodeling and enhancement industry for homes, focusing on kitchens and bathrooms, however, we can remodel or enhance every room in a home, an office space, etc.

The company's name is VELMOR HOME DESIGN, LLC

We'll focus on clients in the Rio Grande Valley, Texas. Primarily McAllen, Edinburg, Pharr, Mission, Brownsville and South Padre Island.

The design on the business card should transmit reliability, professionalism anda bit of upscale design.

The logo is in black and white, and would like to keep it that way.

The information that needs to be printed in the business cards is:
Company's name: Velmor Home Design
Company's Logo (attached)
My name: Noel Bramwit
Address, phone and email:
2715 N Parkline Road, Ste 348
Ashcombe, ZZ 00123
(555) 010 0187
nbramwit@velmordesign.example
Website: velmordesign.example

```html
<!DOCTYPE html>
<html lang="en">
<head>
<meta charset="utf-8">
<title>Velmor Home Design — Business Card</title>
<link rel="stylesheet" href="https://fonts.googleapis.com/css2?family=Montserrat:wght@400;700&family=Questrial&display=swap">
<style>
  :root {
    --backdrop: #5a5a5a;
    --card-dark: #1c1a1a;
    --card-light: #ffffff;
    --ink: #1a1a1a;
    --ink-soft: #3a3a3a;
    --paper-text: #f4f4f4;
    --rule: #6a6a6a;
  }
  * { box-sizing: border-box; margin: 0; padding: 0; }
  html, body { width: 1200px; height: 900px; overflow: hidden; }
  body {
    background: var(--backdrop);
    display: flex;
    flex-direction: column;
    align-items: center;
    justify-content: center;
    gap: 40px;
  }
  .card {
    position: relative;
    width: 665px;
    height: 380px;
    border-radius: 34px;
    box-shadow: 0 10px 28px rgba(0,0,0,.35);
    overflow: hidden;
  }
  .card--front { background: var(--card-dark); }
  .card--back { background: var(--card-light); }

  .brand {
    position: absolute;
    display: flex;
    align-items: center;
    gap: 16px;
  }
  .brand__square {
    width: 46px;
    height: 46px;
    border: 3px solid currentColor;
  }
  .brand__name {
    font-family: "Montserrat", sans-serif;
    font-weight: 400;
    font-size: 17px;
    line-height: 1.12;
    letter-spacing: 0.32em;
    text-transform: uppercase;
  }
  .card--front .brand {
    color: var(--paper-text);
    left: 50%;
    top: 50%;
    transform: translate(-50%, -50%);
  }
  .card--back .brand {
    color: var(--ink);
    left: 42px;
    top: 40px;
  }

  .holder-name {
    position: absolute;
    right: 350px;
    top: 290px;
    font-family: "Montserrat", sans-serif;
    font-weight: 700;
    font-size: 24px;
    letter-spacing: 0.03em;
    color: var(--ink);
    text-transform: uppercase;
    white-space: nowrap;
  }
  .divider {
    position: absolute;
    left: 330px;
    top: 140px;
    width: 1px;
    height: 200px;
    background: var(--rule);
  }
  .contact-list {
    position: absolute;
    left: 348px;
    top: 140px;
    width: 290px;
    list-style: none;
    font-family: "Questrial", sans-serif;
    font-size: 17px;
    color: var(--ink-soft);
  }
  .contact-list li {
    display: flex;
    align-items: flex-start;
    gap: 10px;
    margin-bottom: 13px;
    line-height: 1.25;
    white-space: nowrap;
  }
  .contact-list svg {
    flex: none;
    width: 16px;
    height: 16px;
    margin-top: 2px;
    fill: var(--ink);
  }
</style>
</head>
<body>
  <section class="card card--front" aria-label="Card front">
    <div class="brand">
      <span class="brand__square"></span>
      <span class="brand__name">Velmor<br>Home<br>Design</span>
    </div>
  </section>

  <section class="card card--back" aria-label="Card back">
    <div class="brand">
      <span class="brand__square"></span>
      <span class="brand__name">Velmor<br>Home<br>Design</span>
    </div>

    <p class="holder-name">Noel Bramwit</p>
    <span class="divider"></span>

    <ul class="contact-list">
      <li>
        <svg viewBox="0 0 16 16" aria-hidden="true"><path d="M3 2h3l1.5 3.5-2 1.2a8 8 0 0 0 3.8 3.8l1.2-2L14 10v3a1.5 1.5 0 0 1-1.5 1.5A11.5 11.5 0 0 1 1.5 3.5 1.5 1.5 0 0 1 3 2z"/></svg>
        <span>(555) 010 0187</span>
      </li>
      <li>
        <svg viewBox="0 0 16 16" aria-hidden="true"><path d="M8 1a7 7 0 1 0 0 14A7 7 0 0 0 8 1zm0 1.6c.9 0 1.9 1.7 2.2 4.6H5.8C6.1 4.3 7.1 2.6 8 2.6zM2.7 7.2a5.4 5.4 0 0 1 3-4c-.5 1-.9 2.4-1 4zm0 1.6h2c.1 1.6.5 3 1 4a5.4 5.4 0 0 1-3-4zm5.3 4.6c-.9 0-1.9-1.700-2.2-4.6h4.4c-.3 2.9-1.3 4.6-2.2 4.6zm2.3-.6c.5-1 .9-2.4 1-4h2a5.4 5.4 0 0 1-3 4zm1-5.6c-.1-1.6-.5-3-1-4a5.4 5.4 0 0 1 3 4z"/></svg>
        <span>velmordesign.example</span>
      </li>
      <li>
        <svg viewBox="0 0 16 16" aria-hidden="true"><path d="M1 3.5h14v9H1zm1.5 1.2v.3L8 8.8 13.5 5v-.3zm0 2.1v4.5h11V6.8L8 10.6z"/></svg>
        <span>nbramwit@velmordesign.example</span>
      </li>
      <li>
        <svg viewBox="0 0 16 16" aria-hidden="true"><path d="M8 0.8a5 5 0 0 0-5 5c0 3.8 5 9.4 5 9.4s5-5.6 5-9.4a5 5 0 0 0-5-5zm0 7a2 2 0 1 1 0-4 2 2 0 0 1 0 4z"/></svg>
        <span>2715 N Parkline Road, Ste 348<br>Ashcombe, ZZ 00123</span>
      </li>
    </ul>
  </section>
</body>
</html>
```